The Pulp Corner- 2026 Menu- Drinks/Food

We are The Pulp Corner, a premium NYC-inspired juice bar.
We need two matching 4K TV menu designs with a clean, modern New York feel.
TV 1 – DRINKS
Cold-Pressed Juices, Smoothies, and Coffee/Espresso.
TV 2 – FOOD
Bowls, Toasts, Wraps, Hot Food, and Treats/Sweets.
The menus should feel bold, minimal, and easy to read from a distance.
Strong typography is preferred over heavy photos. The two screens must clearly match as one brand while serving different purposes.
Designs must be optimized for 4K TVs and in a NYC style (subtle subway / street influence, not cartoonish).
This is what we have now. We are updating items and prices along with changing some items.
I have some changes we’d like to do also. But this is what we are using now

```html
<!DOCTYPE html>
<html lang="en">
<head>
<meta charset="utf-8">
<title>The Pulp Corner – Drinks &amp; Food Menu</title>
<link href="https://fonts.googleapis.com/css2?family=Oswald:wght@600&family=Poppins:wght@400;700;800&family=Roboto+Slab:wght@700&display=swap" rel="stylesheet">
<style>
:root{
  --stage:#8f9190;
  --paper:#f7f8ee;
  --leaf:#dfe9cf;
  --green:#6f8a1f;
  --green-dark:#58701a;
  --ink:#3b3b35;
  --muted:#55554d;
  --white:#ffffff;
}
*{margin:0;padding:0;box-sizing:border-box}
html,body{width:950px;height:1200px;overflow:hidden;background:var(--stage)}
body{position:relative;font-family:'Poppins',sans-serif;color:var(--ink)}

.board{position:absolute;left:100px;width:749px;height:421px;background:
  radial-gradient(ellipse 90px 70px at 20px 10px,var(--leaf),transparent 70%),
  radial-gradient(ellipse 80px 60px at 735px 400px,var(--leaf),transparent 70%),
  radial-gradient(ellipse 60px 40px at 330px 400px,#eef3e3,transparent 70%),
  var(--paper);box-shadow:0 4px 10px rgba(0,0,0,.35);overflow:hidden}
.board--drinks{top:72px}
.board--food{top:575px}

.menu-box{position:absolute;border:1.5px solid var(--green);border-radius:4px;padding:8px 10px}
.menu-box::before{content:"";position:absolute;inset:3px;border:1px dashed var(--green);border-radius:3px;pointer-events:none}
.section-title{font-family:'Roboto Slab',serif;font-weight:700;color:var(--green);font-size:16px;text-align:center;line-height:1;margin-bottom:7px}
.cols{display:flex;gap:12px}
.col{flex:1;display:flex;flex-direction:column}

.item{display:grid;grid-template-columns:1fr auto;column-gap:4px;margin-bottom:6px}
.item-name{font-weight:800;font-size:7px;color:var(--green);text-transform:uppercase;line-height:1.1}
.item-desc{grid-column:1;font-size:5.2px;line-height:1.22;color:var(--muted)}
.price{grid-column:2;grid-row:1/span 2;align-self:start;background:var(--green);color:var(--white);font-size:6px;font-weight:700;border-radius:2px;padding:1px 4px;box-shadow:0 0 0 1px var(--white),0 0 0 1.8px var(--green);white-space:nowrap;margin-top:1px}
.price sup{font-size:3.6px}

.brand{position:absolute;left:298px;width:155px;top:40px;text-align:center}
.brand-mark{width:16px;height:16px;border-radius:50%;background:var(--green);margin:0 auto 4px}
.brand-name{font-family:'Roboto Slab',serif;font-weight:700;font-size:19px;color:var(--green-dark);line-height:1}
.board-title{position:absolute;left:270px;width:210px;top:126px;text-align:center;font-family:'Oswald',sans-serif;font-weight:600;font-size:29px;color:#4c5442;letter-spacing:.3px;line-height:1;white-space:nowrap;transform:scaleY(1.15)}

.feature{position:absolute;z-index:2;left:298px;width:155px;top:166px;background:var(--green);border-radius:8px;padding:10px 9px;color:var(--white)}
.feature .section-title{color:var(--white);margin-bottom:9px}
.feature .item-name,.feature .item-desc{color:var(--white)}
.feature .price{background:var(--white);color:var(--green);box-shadow:0 0 0 1px var(--green),0 0 0 1.6px var(--white)}
.feature .item{margin-bottom:8px}

.size-row{display:grid;grid-template-columns:1fr 30px 30px;column-gap:3px;align-items:center;font-size:6.2px;font-weight:400;margin-bottom:5px;white-space:nowrap}
.size-row .price{grid-column:3;grid-row:auto;justify-self:end;margin-top:0}
.size-row .label{font-weight:800;font-size:6px;text-transform:uppercase}
.size-row .item-desc{white-space:normal}

.photo{position:absolute;border-radius:10px}
.web{position:absolute;font-weight:700;font-size:12.5px;letter-spacing:1.6px;color:var(--ink)}
.web span{color:var(--green)}
.note{font-size:5.2px;color:var(--muted);line-height:1.2}
.note b{display:block;font-size:7px;color:var(--green);font-weight:800}

.sub-title{position:absolute;font-family:'Roboto Slab',serif;font-weight:700;font-size:17px;color:var(--green)}
.hot-grid{position:absolute;left:42px;top:322px;width:235px;display:grid;grid-template-columns:1fr 1fr;column-gap:16px}

.social{position:absolute;top:382px;display:flex;align-items:center;gap:5px;font-weight:700;font-size:10px;color:var(--ink)}
.social i{width:8px;height:8px;border-radius:50%;background:var(--ink);display:block}
</style>
</head>
<body>

<section class="board board--drinks">
  <div class="menu-box" style="left:40px;top:40px;width:249px;height:216px">
    <h2 class="section-title">Cold Pressed Juices</h2>
    <div class="cols">
      <div class="col">
        <div class="item"><div class="item-name">Hot Bam (s)</div><div class="item-desc">Red Apple, Lemon, Ginger, Cayenne Pepper</div><div class="price"><sup>$</sup>12.50</div></div>
        <div class="item"><div class="item-name">Sunset Park</div><div class="item-desc">Spinach, Celery, Cucumber, Romaine, Lemon, Himalayan Pink Salt</div><div class="price"><sup>$</sup>12.60</div></div>
        <div class="item"><div class="item-name">Revive</div><div class="item-desc">Cantaloupe, Red Apple, Lemon</div><div class="price"><sup>$</sup>12.50</div></div>
        <div class="item"><div class="item-name">Vida</div><div class="item-desc">Beet, Raspberry, Red Apple, Orange</div><div class="price"><sup>$</sup>12.50</div></div>
        <div class="item"><div class="item-name">The Breakdown</div><div class="item-desc">Carrot, Red Apple, Ginger, Beet, Lemon, Pineapple</div><div class="price"><sup>$</sup>12.50</div></div>
        <div class="item"><div class="item-name">Green Goddess</div><div class="item-desc">Spinach, Celery, Cucumber, Romaine, Kale, Parsley, Green Cabbage</div><div class="price"><sup>$</sup>12.50</div></div>
      </div>
      <div class="col">
        <div class="item"><div class="item-name">Sunny Day</div><div class="item-desc">Pineapple, Lemon, Orange, Ginger</div><div class="price"><sup>$</sup>12.50</div></div>
        <div class="item"><div class="item-name">Glow Up</div><div class="item-desc">Celery, Lime</div><div class="price"><sup>$</sup>12.50</div></div>
        <div class="item"><div class="item-name">Sailor's Delight</div><div class="item-desc">Spinach, Orange, Pear, Green Apple, Ginger</div><div class="price"><sup>$</sup>12.50</div></div>
        <div class="item"><div class="item-name">Classic (shot)</div><div class="item-desc">Ginger, Lemon</div><div class="price"><sup>$</sup>12.50</div></div>
        <div class="item"><div class="item-name">Sunshine (shot)</div><div class="item-desc">Ginger, Lemon, Red Apple, Turmeric, Black Pepper</div><div class="price"><sup>$</sup>12.50</div></div>
        <div class="item"><div class="item-name">Titan (shot)</div><div class="item-desc">Wheatgrass</div><div class="price"><sup>$</sup>12.50</div></div>
      </div>
    </div>
  </div>
  <div class="photo" role="img" aria-label="Glasses of fresh juice and smoothies with berries, strawberries and a lime margarita glass" style="left:50px;top:258px;width:240px;height:108px;background:radial-gradient(ellipse at 55% 50%,#c97a6e 0%,#b77a3e 35%,#6d7a2c 60%,transparent 75%)"></div>
  <div class="web" style="left:63px;top:368px">www.<span>thepulpcorner</span>.net</div>

  <div class="brand"><div class="brand-mark"></div><div class="brand-name">The Pulp Corner</div></div>
  <h1 class="board-title">DRINKS MENU</h1>

  <div class="feature" style="height:195px">
    <h2 class="section-title">More Cold Drinks</h2>
    <div class="size-row"><span class="label">Cold Brew Coffee</span><span>(12 oz)</span><span class="price"><sup>$</sup>5.50</span></div>
    <div class="size-row"><span></span><span>(16 oz)</span><span class="price"><sup>$</sup>7.50</span></div>
    <div class="size-row"><span class="item-desc">Almond Milk, Coconut Milk, Agave or Vanilla</span><span>(each) +</span><span class="price"><sup>$</sup>0.75</span></div>
    <div class="photo" role="img" aria-label="Cup of black coffee on a saucer with coffee beans" style="position:relative;margin:4px auto 8px;width:95px;height:46px;background:radial-gradient(ellipse at 50% 55%,#ffffff 0%,#e6e6e0 45%,transparent 72%)"></div>
    <div class="size-row"><span class="label">Alkaline Water</span><span></span><span class="price"><sup>$</sup>3.00</span></div>
    <div class="size-row"><span class="label">Coconut Water</span><span></span><span class="price"><sup>$</sup>5.50</span></div>
  </div>
  <div class="photo" role="img" aria-label="Halved coconut beside a glass of coconut water" style="left:335px;top:345px;width:105px;height:52px;background:radial-gradient(ellipse at 40% 55%,#6e4a30 0%,#a98560 40%,transparent 72%)"></div>

  <div class="menu-box" style="left:467px;top:40px;width:248px;height:338px">
    <h2 class="section-title">Smoothies</h2>
    <div class="cols">
      <div class="col">
        <div class="item"><div class="item-name">Spring Street</div><div class="item-desc">Coconut Water, Blueberries, Pineapple, Spinach, Honey, Hemp Hearts</div><div class="price"><sup>$</sup>13.00</div></div>
        <div class="item"><div class="item-name">Flushing Ave</div><div class="item-desc">Coconut Milk, Spinach, Kale, Strawberries, Pineapple, Chia Seeds, Hemp Hearts</div><div class="price"><sup>$</sup>13.00</div></div>
        <div class="item"><div class="item-name">Fort Greene</div><div class="item-desc">Almond Milk, Bananas, Mango, Avocado, Spinach, Kale, Honey</div><div class="price"><sup>$</sup>13.00</div></div>
        <div class="item"><div class="item-name">Jimmy the Green Machine</div><div class="item-desc">Coconut Milk, Bananas, Strawberries, Kale, Sea Moss Gel, Green Spirulina</div><div class="price"><sup>$</sup>13.00</div></div>
        <div class="item"><div class="item-name">Atlantic Terminal</div><div class="item-desc">Almond Milk, Bananas, Strawberries, Blueberries, Pineapple, Coconut Shavings; Choice of 1 of the following: Peanut, Almond, Cashew Butter and/or Hazelnut Spread, Honey, Chia Seeds, Bee Pollen</div><div class="price"><sup>$</sup>13.00</div></div>
        <div class="item"><div class="item-name">Union Square</div><div class="item-desc">Almond Milk, Grade A Açaí, Bananas, Strawberries, Blueberries, Pineapple, Coconut Oil</div><div class="price"><sup>$</sup>13.00</div></div>
        <div class="item"><div class="item-name">Build Your Own</div><div class="item-desc">1 liquid base: Almond, Coconut, Oat Milk, Orange, Apple Juice, Coconut Water, Filtered Water; Choice of 3 Fruits and /or Vegetables.</div><div class="price"><sup>$</sup>12.00</div></div>
      </div>
      <div class="col">
        <div class="item"><div class="item-name">Grand Central</div><div class="item-desc">Almond Milk, Grade A Açaí, Bananas, Blueberries, Granola, Cacao Nibs; Choice of 1 of the following: Peanut, Almond, Cashew Butter and/or Hazelnut Spread</div><div class="price"><sup>$</sup>13.00</div></div>
        <div class="item"><div class="item-name">P.S. 124</div><div class="item-desc">1 liquid base: Almond, Coconut and/or Oat Milk, Orange Juice, Apple Juice or Coconut Water; Bananas</div><div class="price"><sup>$</sup>12.00</div></div>
        <div class="item"><div class="item-name">Lexington Avenue</div><div class="item-desc">Coconut Milk, Strawberries, Bananas, Raspberries, Kiwi, Vanilla Yogurt</div><div class="price"><sup>$</sup>12.50</div></div>
        <div class="item"><div class="item-name">Power Up</div><div class="item-desc">Almond Milk, Bananas, Strawberries, Raspberries, Peanut Butter, Cacao Nibs</div><div class="price"><sup>$</sup>13.00</div></div>
        <div class="item"><div class="item-name">The "Cawfee" Smoothie</div><div class="item-desc">Cold Brew Coffee, Almond Milk, Bananas, Vanilla Plant Protein, Cacao Nibs, Agave</div><div class="price"><sup>$</sup>13.00</div></div>
        <div class="item"><div class="item-name">The Peanut</div><div class="item-desc">Almond Milk, Bananas, Peanut Butter, Cinnamon, Chocolate Plant Protein</div><div class="price"><sup>$</sup>12.50</div></div>
        <div class="photo" role="img" aria-label="Tall glass of layered red and orange smoothie with a lemon slice" style="position:relative;margin:4px 0 0 60px;width:40px;height:70px;background:linear-gradient(180deg,transparent 0%,#f0b43a 30%,#e0452a 75%,transparent 100%)"></div>
      </div>
    </div>
  </div>
</section>

<section class="board board--food">
  <div class="menu-box" style="left:40px;top:40px;width:249px;height:240px">
    <h2 class="section-title">Bowls</h2>
    <div class="cols">
      <div class="col">
        <div class="item"><div class="item-name">Park Slope</div><div class="item-desc">Grade A Açaí, Granola, Bananas, Honey</div><div class="price"><sup>$</sup>13.00</div></div>
        <div class="item"><div class="item-name">Bay Ridge</div><div class="item-desc">Grade A Açaí, Granola, Bananas, Strawberries, Blueberries, Honey</div><div class="price"><sup>$</sup>14.00</div></div>
        <div class="item"><div class="item-name">Bushwick</div><div class="item-desc">Grade A Açaí, Granola, Bananas, Pineapple, Fresh Coconut Meat, Honey, Bee Pollen</div><div class="price"><sup>$</sup>14.00</div></div>
        <div class="item"><div class="item-name">Main Street</div><div class="item-desc">Grade A Açaí, Choice of 1 of the following: Peanut, Almond, Cashew Butter and/or Hazelnut Spread, Granola, Bananas, Honey, Cacao Nibs, Hemp Hearts</div><div class="price"><sup>$</sup>14.00</div></div>
        <div class="item"><div class="item-name">Coney Island</div><div class="item-desc">Apple Juice blended w/ Jackfruit, Mango and Pineapple, Layered w/ Granola, Bananas, Strawberries, Pineapple, Honey</div><div class="price"><sup>$</sup>14.00</div></div>
      </div>
      <div class="col">
        <div class="item"><div class="item-name">The Village</div><div class="item-desc">Grade A Açaí, Granola, Bananas, Strawberries, Kiwi, Pineapple, Blueberries, Coconut Shavings, Honey, Hemp Hearts</div><div class="price"><sup>$</sup>14.00</div></div>
        <div class="item"><div class="item-name">Build Your Own</div><div class="item-desc">Grade A Açaí, Granola, 2 Organic Fruits, Honey</div><div class="price"><sup>$</sup>14.00</div></div>
        <div class="item"><div class="item-name">Pink Prowler</div><div class="item-desc">Apple Juice blended w/ Pitaya, Bananas, Strawberries, Layered w/ Granola, Strawberries, Pineapple, Blueberries, Coconut Flakes, Honey, Hemp Hearts</div><div class="price"><sup>$</sup>14.00</div></div>
        <div class="item"><div class="item-name">Coco Loco</div><div class="item-desc">Coconut Milk blended w/ Coconut Chunks, Bananas, Honey, Layered w/ Granola, Pineapple, Seasonal Fruit, Fresh Coconut Meat, Coconut Flakes, Honey, Hemp Hearts</div><div class="price"><sup>$</sup>14.00</div></div>
      </div>
    </div>
  </div>
  <div class="photo" role="img" aria-label="Bowl of fresh green salad" style="left:38px;top:268px;width:64px;height:40px;background:radial-gradient(ellipse at 50% 55%,#7aa23c 0%,#3a3a36 55%,transparent 72%)"></div>
  <div class="photo" role="img" aria-label="Poke bowl with salmon, mango, cucumber and pickled onion" style="left:210px;top:255px;width:80px;height:52px;background:radial-gradient(ellipse at 50% 50%,#e8894a 0%,#b9c86a 40%,#eef1f4 60%,transparent 74%)"></div>

  <h2 class="sub-title" style="left:122px;top:290px">Hot Food</h2>
  <div class="hot-grid">
    <div class="item"><div class="item-name">Park Slope</div><div class="item-desc">Grade A Açaí, Granola, Bananas, Honey</div><div class="price"><sup>$</sup>13.00</div></div>
    <div class="item"><div class="item-name">Park Slope</div><div class="item-desc">Grade A Açaí, Granola, Bananas, Honey</div><div class="price"><sup>$</sup>13.00</div></div>
    <div class="item"><div class="item-name">Park Slope</div><div class="item-desc">Grade A Açaí, Granola, Bananas, Honey</div><div class="price"><sup>$</sup>13.00</div></div>
    <div class="item"><div class="item-name">Park Slope</div><div class="item-desc">Grade A Açaí, Granola, Bananas, Honey</div><div class="price"><sup>$</sup>13.00</div></div>
  </div>
  <div class="web" style="left:46px;top:381px">www.<span>thepulpcorner</span>.net</div>

  <div class="brand"><div class="brand-mark"></div><div class="brand-name">The Pulp Corner</div></div>
  <h1 class="board-title">FOOD MENU</h1>

  <div class="feature" style="height:190px">
    <h2 class="section-title">Treats</h2>
    <div class="item"><div class="item-name">Captain Berry</div><div class="item-desc">Vanilla Yogurt, Granola, Strawberries, Blueberries, Coconut Flakes, Honey, Hemp Hearts</div><div class="price"><sup>$</sup>9.00</div></div>
    <div class="item"><div class="item-name">Build Your<br>Own Parfait</div><div class="item-desc">Vanilla Yogurt, Granola, Choice of 2 Fruits, Honey</div><div class="price"><sup>$</sup>8.00</div></div>
    <div class="item"><div class="item-name">Protein Bites</div><div class="item-desc">Gluten Free Oats, Peanut Butter, Chia, Cacao Flax, Goji Berries, Chocolate Plant Protein, Maple Syrup &amp; Vanilla</div><div class="price"><sup>$</sup>6.25</div></div>
    <div class="item"><div class="item-name">Overnight Oats</div><div class="item-desc">Coconut Milk, Greek Yogurt, Chia Seeds, Vanilla Extract, Maple Syrup, Choice of 2 Fruit Toppings, Coconut Flakes, Honey, Cinnamon</div><div class="price"><sup>$</sup>9.00</div></div>
  </div>
  <div class="photo" role="img" aria-label="Plates of sliced wraps with dipping sauce" style="left:280px;top:356px;width:190px;height:44px;background:radial-gradient(ellipse at 28% 50%,#d9b58a 0%,#2d2d2a 45%,transparent 62%),radial-gradient(ellipse at 72% 50%,#8fae4c 0%,#2d2d2a 45%,transparent 62%)"></div>

  <div class="menu-box" style="left:467px;top:40px;width:248px;height:250px">
    <h2 class="section-title">Toasts &amp; Wraps</h2>
    <div class="cols">
      <div class="col">
        <div class="item"><div class="item-name">The Patriot</div><div class="item-desc">Seedy Sourdough Bread, Choice of Peanut, Almond, Cashew Butter or Hazelnut Spread, Strawberries, Bananas, Blueberries, Honey, Hemp Hearts</div><div class="price"><sup>$</sup>13.00</div></div>
        <div class="item"><div class="item-name">Avocado Toast</div><div class="item-desc">Seedy Sourdough Bread, Whole Avocado, Everything Bagel Seasoning, Honey</div><div class="price"><sup>$</sup>13.00</div></div>
        <div class="item"><div class="item-name">Breakfast Toast</div><div class="item-desc">Seedy Sourdough Bread, Smashed Avocado, Hard Boiled Eggs, Red Onion, Lemon Juice, Himalayan Pink Salt, Pepper, Everything Bagel Seasoning</div><div class="price"><sup>$</sup>13.00</div></div>
        <div class="item"><div class="item-name">Smoked Salmon<br>Toast</div><div class="item-desc">Seedy Sourdough Bread, Smoked Wild Salmon, Tamari Sauce, Avocado, Cucumber, Leafy Greens, Everything Bagel Seasoning</div><div class="price"><sup>$</sup>13.00</div></div>
      </div>
      <div class="col">
        <div class="item"><div class="item-name">Turmeric<br>Chicken Salad</div><div class="item-desc">Wholewheat Sprouted Grain Wrap, Mayo, Chicken Breast, Red Onion, Cucumber, Carrots, Leafy Greens, Served with Balsamic Vinegar</div><div class="price"><sup>$</sup>13.00</div></div>
        <div class="item"><div class="item-name">Elite Wild<br>Tuna Salad</div><div class="item-desc">Wholewheat Sprouted Grain Wrap, Mayo, Wild Tuna, Red Onion, Celery, Leafy Greens</div><div class="price"><sup>$</sup>13.00</div></div>
        <div class="item"><div class="item-name">Spicy Chickpea<br>Salad (V)(S)</div><div class="item-desc">Wholewheat Sprouted Grain Wrap, Tomatillo Sriracha, Chickpeas, Toasted Sesame Seeds, Red Pepper Hummus, Leafy Greens</div><div class="price"><sup>$</sup>13.00</div></div>
        <div class="note"><b>*Custom Salads</b>Available upon request depending on availability</div>
      </div>
    </div>
  </div>
  <div class="photo" role="img" aria-label="Toast with egg, layered chocolate dessert jars and a sandwich with lettuce" style="left:472px;top:292px;width:258px;height:80px;background:radial-gradient(ellipse at 18% 60%,#e3c08a 0%,transparent 45%),radial-gradient(ellipse at 48% 55%,#6b4030 0%,transparent 40%),radial-gradient(ellipse at 80% 50%,#b07a45 0%,#79a23a 25%,transparent 50%)"></div>
  <div class="social" style="left:484px"><i></i>@ThePulpCorner561</div>
  <div class="social" style="left:633px"><i></i>The Pulp Corner</div>
</section>

</body>
</html>
```